Bright Haven Estate Sales web design

We are looking to launch an Estate Sales Website for Nashville, TN. The name of our Business is Bright Haven Estate Sales. We would like to give you a blank slate so that you can showcase your design skills for us. The few things we are looking for are a nice header graphic of a house or a stock image of an estate sale. Near the header graphic we would like a quick inquiry form. If not on the right side of the header maybe midway down the site. We potentially want to see what purple and Gold look like on the site however this is not a must. We have over 20 years of industry related experience.

1. Buttons at top of the website will be.
a. Services
b. Upcoming Sales
c. About Us
d. FAQs
e. Resources

Services we offer:
1. Estate Sales
2. Cleanouts
3. Appraisals

Sites We like:
https://www.corvellestatesales.example/

We don't have a logo yet so if you have ideas please share them with us. Below are 2 ideas however if you have your own thoughts please ignore.

1. Oval ornate frame, gold and black, with BHES in the middle, deep purple. Think of catering to high class people..font should be fancy as opposed to simple.

2. Another option, Bright Haven in bold fancy script, same colors, with Estate Sales below, small different font, black.

```html
<!DOCTYPE html>
<html lang="en">
<head>
<meta charset="utf-8">
<title>Bright Haven Estate Sales</title>
<link href="https://fonts.googleapis.com/css2?family=Poppins:wght@300;400;500;600;700;800&family=Allura&display=swap" rel="stylesheet">
<style>
:root{
  --purple:#2b0a4a;
  --purple-dark:#1f0638;
  --purple-soft:#f3eff6;
  --gold:#e6b52c;
  --gold-light:#f2d36b;
  --ink:#1c1326;
  --muted:#5b5463;
  --line:#d9d2df;
  --white:#ffffff;
}
*{box-sizing:border-box;margin:0;padding:0}
html,body{width:1200px;height:4062px;overflow:hidden}
body{font-family:"Poppins",sans-serif;color:var(--ink);background:var(--white);position:relative}
.btn-gold{background:linear-gradient(90deg,var(--gold-light),var(--gold));color:var(--purple);font-weight:600;font-size:12px;text-transform:uppercase;display:flex;align-items:center;justify-content:center;letter-spacing:.3px}
.brand{font-family:"Poppins",sans-serif;font-weight:700;color:var(--purple);display:flex;align-items:center;gap:8px;line-height:1.05}
.brand-mark{width:14px;height:14px;background:var(--gold);flex:none}

/* header */
.site-header{position:absolute;left:0;top:0;width:1200px;height:62px;background:var(--white)}
.site-header .brand{position:absolute;left:121px;top:9px;font-size:15px;width:130px}
.main-nav{position:absolute;left:265px;top:0;height:62px;display:flex;align-items:center;gap:38px;font-size:13px;font-weight:500}
.main-nav a{color:var(--ink);text-decoration:none}
.main-nav a.active{color:var(--gold)}
.header-phone{position:absolute;left:836px;top:15px;width:130px;height:33px;border:1.5px solid var(--purple);display:flex;align-items:center;justify-content:center;gap:6px;font-size:13px;font-weight:600;color:var(--purple)}
.header-cta{position:absolute;left:973px;top:15px;width:106px;height:33px}

/* hero */
.hero{position:absolute;left:0;top:62px;width:1200px;height:593px;background:linear-gradient(180deg,#5f6a5a 0%,#8a5a4a 45%,#6b3e33 70%,#4e5a3c 100%)}
.hero::after{content:"";position:absolute;inset:0;background:linear-gradient(90deg,rgba(20,10,30,.55),rgba(20,10,30,.1) 60%)}
.hero-text{position:absolute;left:118px;top:160px;z-index:2;color:var(--white)}
.hero-welcome{font-family:"Allura",cursive;font-size:56px;line-height:1}
.hero-title{font-weight:800;font-size:70px;line-height:1.0;margin-top:6px}
.inquiry{position:absolute;left:719px;top:53px;width:360px;height:481px;background:var(--white);z-index:2;border:3px solid var(--purple)}
.inquiry h2{background:var(--purple);color:var(--white);height:80px;display:flex;align-items:center;justify-content:center;font-size:32px;font-weight:700}
.inquiry form{padding:18px 20px 0 23px}
.field{height:36px;border:1.5px solid #b9b0c2;margin-bottom:12px;font-size:11px;padding:0 12px;display:flex;align-items:center;color:var(--ink)}
.field.tall{height:72px;align-items:flex-start;padding-top:10px}
.consent{display:flex;align-items:center;gap:8px;font-size:11px;margin:4px 0 12px}
.consent span{width:22px;height:20px;border:1.5px solid #8c8496;display:block}
.inquiry .btn-gold{height:34px}

/* services */
.services{position:absolute;left:0;top:655px;width:1200px;height:560px;background:linear-gradient(110deg,#f1eef3 0%,#ffffff 35%)}
.section-title{font-weight:700;font-size:32px;text-align:center;color:var(--purple)}
.services .section-title{position:absolute;left:0;width:1200px;top:42px}
.services .intro{position:absolute;left:270px;width:660px;top:83px;text-align:center;font-size:11px;color:var(--muted);line-height:1.45}
.svc-card{position:absolute;top:146px;width:307px;height:292px;border:1.5px solid var(--purple);background:var(--white);text-align:center}
.svc-icon{width:96px;height:96px;border-radius:50%;background:var(--purple);border:3px solid var(--white);outline:2px solid var(--purple);margin:37px auto 0;display:flex;align-items:center;justify-content:center}
.svc-card h3{font-size:19px;font-weight:700;color:var(--purple);margin-top:14px}
.svc-card p{font-size:11px;color:var(--muted);line-height:1.4;padding:4px 28px 0}
.svc-card .more{position:absolute;left:-1.5px;bottom:-1.5px;width:307px;height:40px;background:var(--purple);color:var(--gold);font-size:11px;font-weight:600;display:flex;align-items:center;justify-content:center;gap:8px}
.services .all{position:absolute;left:522px;top:465px;width:155px;height:36px}

/* upcoming */
.upcoming{position:absolute;left:0;top:1215px;width:1200px;height:542px;background:var(--purple);overflow:hidden}
.upcoming .section-title{position:absolute;left:0;width:1200px;top:48px;color:var(--gold)}
.sale-card{position:absolute;top:121px;width:307px;height:304px;background:var(--white)}
.sale-photo{height:230px}
.sale-meta{padding:6px 11px 0}
.sale-meta small{font-size:9px;color:var(--muted);display:block}
.sale-meta h3{font-size:14px;font-weight:600;color:var(--purple);margin-top:2px}
.sale-facts{display:flex;justify-content:space-between;align-items:center;font-size:9.5px;margin-top:8px;color:var(--muted)}
.sale-facts b{color:var(--ink);font-weight:500;font-size:11px}
.dot{display:inline-block;width:8px;height:8px;background:var(--gold);margin-right:3px;vertical-align:-1px}
.upcoming .all{position:absolute;left:535px;top:452px;width:131px;height:35px;z-index:2}
.outline-word{position:absolute;left:0;width:1200px;text-align:center;font-weight:700;color:transparent;-webkit-text-stroke:1.5px;white-space:nowrap;letter-spacing:8px}
.upcoming .outline-word{top:455px;font-size:100px;-webkit-text-stroke-color:rgba(255,255,255,.18)}

/* resources */
.resources-head{position:absolute;left:121px;top:1800px;width:958px;height:55px;border-bottom:1.5px solid var(--purple)}
.resources-head h2{font-size:32px;font-weight:700;color:var(--purple)}
.resources-head .btn-gold{position:absolute;right:0;top:6px;width:162px;height:35px}
.post-lg{position:absolute;left:121px;top:1888px;width:518px;height:407px;background:var(--purple-soft)}
.post-lg .photo{position:absolute;left:16px;top:13px;width:488px;height:275px}
.post-date{display:inline-block;background:var(--purple);color:var(--gold);font-size:11px;padding:2px 12px}
.post-lg .body{position:absolute;left:32px;top:292px;width:440px}
.post-lg h3{font-size:15px;font-weight:600;color:var(--purple);margin-top:8px}
.post-lg p,.post-sm p{font-size:10.5px;color:var(--muted);line-height:1.35;margin-top:3px}
.arrow-btn{position:absolute;width:30px;height:24px;background:var(--purple);display:flex;align-items:center;justify-content:center}
.post-sm{position:absolute;left:659px;width:420px;height:198px;background:var(--purple-soft)}
.post-sm .photo{position:absolute;left:13px;top:14px;width:192px;height:168px}
.post-sm .body{position:absolute;left:218px;top:44px;width:190px}
.post-sm h3{font-size:14.5px;font-weight:600;color:var(--purple);line-height:1.2;margin-top:5px}

/* about */
.about-photo{position:absolute;left:121px;top:2355px;width:958px;height:459px;background:linear-gradient(90deg,#a9b4a0 0%,#c9c3b8 40%,#7c6f68 65%,#c8333a 68%,#d43d3f 100%)}
.about-box{position:absolute;left:153px;top:2661px;width:893px;height:283px;background:var(--purple);border:1.5px solid #d7cce0;outline:3px solid var(--purple);text-align:center;color:#e8e0ee;padding-top:37px}
.about-box h2{font-size:32px;font-weight:700;color:var(--gold)}
.about-box p{font-size:11px;line-height:1.45;width:700px;margin:12px auto 0}
.about-box .btn-gold{width:106px;height:35px;margin:17px auto 0}

/* faq */
.faq-photo-frame{position:absolute;left:143px;top:2997px;width:433px;height:375px;border:1.5px solid var(--purple);padding:7px}
.faq-photo{width:100%;height:100%;background:linear-gradient(160deg,#4d7a45 0%,#8fa878 45%,#c7a77a 75%,#8a6a48 100%)}
.faq{position:absolute;left:609px;top:3014px;width:470px}
.faq h2{font-size:31px;font-weight:700;color:var(--purple);white-space:nowrap}
.faq-open{margin-top:14px;border:1.5px solid #e3dde8;padding:11px 17px 16px}
.faq-q{display:flex;justify-content:space-between;font-size:11px;font-weight:600;color:var(--purple)}
.faq-open p{font-size:10.5px;color:var(--muted);line-height:1.4;margin-top:6px}
.faq-item{height:36px;border-bottom:1.5px solid var(--line);display:flex;align-items:center;justify-content:space-between;font-size:11px;font-weight:600;color:var(--purple);padding:0 5px}
.faq-item span::before{content:"";display:inline-block;width:6px;height:6px;border-radius:50%;background:var(--purple);margin-right:10px;vertical-align:1px}
.wordmark-band{top:3432px;font-size:56px;font-weight:500;-webkit-text-stroke-color:#9e97a6;letter-spacing:5px}

/* newsletter */
.newsletter{position:absolute;left:0;top:3509px;width:1200px;height:300px;background:linear-gradient(180deg,#3a1a5a,#2b0a4a 60%,#2f1450);text-align:center;color:var(--white)}
.newsletter h2{font-size:33px;font-weight:500;line-height:1.2;margin-top:72px}
.subscribe{width:553px;height:44px;border:1.5px solid #cfc4da;margin:29px auto 0;display:flex;align-items:center;justify-content:space-between;padding:0 6px 0 17px;font-size:12px}
.subscribe .btn-gold{width:107px;height:32px}

/* footer */
.site-footer{position:absolute;left:0;top:3809px;width:1200px;height:253px}
.site-footer .brand{position:absolute;left:121px;top:40px;font-size:20px;width:170px}
.foot-about{position:absolute;left:121px;top:100px;width:150px;font-size:10px;color:var(--muted);line-height:1.4}
.foot-col{position:absolute;top:36px;padding-left:22px;border-left:1.5px solid var(--line);height:145px}
.foot-col h4{font-size:17px;font-weight:600;color:var(--purple);margin-bottom:8px}
.foot-col li{list-style:none;font-size:9.5px;color:var(--muted);line-height:16.5px;display:flex;align-items:center;gap:8px}
.ico{width:15px;height:15px;border-radius:50%;background:var(--purple);flex:none}
.foot-rule{position:absolute;left:121px;top:191px;width:958px;border-top:1.5px solid var(--purple)}
.copyright{position:absolute;left:0;top:207px;width:1200px;text-align:center;font-size:9.5px;color:var(--muted)}
</style>
</head>
<body>

<header class="site-header">
  <div class="brand"><span class="brand-mark"></span><span>Bright Haven Estate Sales</span></div>
  <nav class="main-nav">
    <a class="active" href="#">Home</a><a href="#">Services</a><a href="#">Upcoming Sales</a><a href="#">About Us</a><a href="#">FAQs</a><a href="#">Resources</a>
  </nav>
  <div class="header-phone">
    <svg width="13" height="13" viewBox="0 0 24 24"><path fill="#e6b52c" d="M6.6 10.8a15.5 15.5 0 0 0 6.6 6.6l2.2-2.2c.3-.3.7-.4 1-.2 1.1.4 2.3.6 3.6.6.6 0 1 .4 1 1V20c0 .6-.4 1-1 1A17 17 0 0 1 3 4c0-.6.4-1 1-1h3.5c.6 0 1 .4 1 1 0 1.3.2 2.5.6 3.6.1.3 0 .7-.2 1z"/></svg>
    615-555-0142
  </div>
  <div class="header-cta btn-gold">Contact Us</div>
</header>

<section class="hero">
  <div role="img" aria-label="Photo of a large brick family home with a front lawn and trees" style="position:absolute;inset:0"></div>
  <div class="hero-text">
    <div class="hero-welcome">Welcome To</div>
    <h1 class="hero-title">Bright Haven<br>Estate Sales</h1>
  </div>
  <aside class="inquiry">
    <h2>Get In Touch</h2>
    <form>
      <div class="field">Name</div>
      <div class="field">Email</div>
      <div class="field">Phone</div>
      <div class="field">Address</div>
      <div class="field tall">Message</div>
      <div class="consent"><span></span>I agree to your communication and usage terms</div>
      <div class="btn-gold">Contact Us</div>
    </form>
  </aside>
</section>

<section class="services">
  <h2 class="section-title">Our Services</h2>
  <p class="intro">Lorem ipsum dolor sit amet, consectetur adipiscing elit. Ut non est mi. Vivamus luctus mi in odio volutpat, interdum bibendum magna commodo. Proin nec molestie lorem, et gravida enim. Proin iaculis et lorem a molestie.</p>

  <article class="svc-card" style="left:121px">
    <div class="svc-icon"><svg width="44" height="44" viewBox="0 0 24 24" fill="none" stroke="#e6b52c" stroke-width="1.4"><path d="M3 11 12 3l9 8M5 9.5V21h14V9.5"/><path d="M10 21v-5h4v5"/></svg></div>
    <h3>Estate Sales</h3>
    <p>Each estate sale company offers a slightly different menu of servicesand fees.</p>
    <div class="more">VIEW SERVICES <svg width="18" height="8" viewBox="0 0 18 8"><path d="M0 4h16M13 1l3 3-3 3" stroke="#fff" fill="none"/></svg></div>
  </article>
  <article class="svc-card" style="left:446px">
    <div class="svc-icon"><svg width="44" height="44" viewBox="0 0 24 24" fill="none" stroke="#e6b52c" stroke-width="1.4"><path d="M14 3l7 7-9 9-7-7z"/><path d="M3 21l4-4M9 9l6 6"/></svg></div>
    <h3>Cleanouts</h3>
    <p>Cleanout Services also Include Rearranging Furniture between rooms, in your garage and Educated Suggestions During the Process.</p>
    <div class="more">VIEW SERVICES <svg width="18" height="8" viewBox="0 0 18 8"><path d="M0 4h16M13 1l3 3-3 3" stroke="#fff" fill="none"/></svg></div>
  </article>
  <article class="svc-card" style="left:771px">
    <div class="svc-icon"><svg width="44" height="44" viewBox="0 0 24 24" fill="none" stroke="#e6b52c" stroke-width="1.4"><path d="M3 11 12 3l9 8M5 9.5V21h14V9.5"/><circle cx="12" cy="14" r="3"/><path d="M14 16l2.5 2.5"/></svg></div>
    <h3>Appraisals</h3>
    <p>An Appraisal is a valuation of property, such as Real estate, a Business, collectible, or an Antique, by the Estimate of an authorized Person.</p>
    <div class="more">VIEW SERVICES <svg width="18" height="8" viewBox="0 0 18 8"><path d="M0 4h16M13 1l3 3-3 3" stroke="#fff" fill="none"/></svg></div>
  </article>
  <div class="all btn-gold">View All Services</div>
</section>

<section class="upcoming">
  <h2 class="section-title">Upcoming Sales</h2>
  <article class="sale-card" style="left:121px">
    <div class="sale-photo" role="img" aria-label="Photo of a grey-blue colonial house with a red door and garden" style="background:linear-gradient(180deg,#b9cde0 0%,#4f5d70 45%,#5f8a3e 80%,#4f7a30 100%)"></div>
    <div class="sale-meta"><small>Maplewood Hills, TN 37201</small><h3>Maplewood Hills Estate Sale</h3>
      <div class="sale-facts"><span><i class="dot"></i>4.5 Rooms &nbsp; <i class="dot"></i>3 Bedrooms</span><b>$ 1,500.00 USD/month</b></div></div>
  </article>
  <article class="sale-card" style="left:446px">
    <div class="sale-photo" role="img" aria-label="Photo of a craftsman style home with a wide green lawn" style="background:linear-gradient(180deg,#3f86c8 0%,#8fb8d9 35%,#56636e 55%,#5e9a2e 75%,#4a8424 100%)"></div>
    <div class="sale-meta"><small>Maplewood Hills, TN 37201</small><h3>Maplewood Hills Estate Sale</h3>
      <div class="sale-facts"><span><i class="dot"></i>4.5 Rooms &nbsp; <i class="dot"></i>3 Bedrooms</span><b>$ 1,500.00 USD/month</b></div></div>
  </article>
  <article class="sale-card" style="left:771px">
    <div class="sale-photo" role="img" aria-label="Photo of a modern two-storey home lit at dusk" style="background:linear-gradient(180deg,#a7c3d8 0%,#6f7e88 40%,#3a342e 65%,#9a8e82 100%)"></div>
    <div class="sale-meta"><small>Maplewood Hills, TN 37201</small><h3>Maplewood Hills Estate Sale</h3>
      <div class="sale-facts"><span><i class="dot"></i>4.5 Rooms &nbsp; <i class="dot"></i>3 Bedrooms</span><b>$ 1,500.00 USD/month</b></div></div>
  </article>
  <div class="outline-word">UPCOMING SALES</div>
  <div class="all btn-gold">View All Sales</div>
</section>

<div class="resources-head">
  <h2>Our Resources</h2>
  <div class="btn-gold">View All Resources</div>
</div>

<article class="post-lg">
  <div class="photo" role="img" aria-label="Photo of a handshake over a small model house on a desk" style="background:linear-gradient(120deg,#6f8f4c 0%,#d8cfc2 35%,#f0e6da 60%,#c98e5c 100%)"></div>
  <div class="body">
    <span class="post-date">December 13, 2022</span>
    <h3>Building A Better World: Can Architecture Shape Behaviour?</h3>
    <p>Lorem ipsum dolor sit amet, consectetur adipiscing elit. Ut non est mi. Vivamus luctus mi in odio volutpat, interdum bibendum magna commodo. Proin nec molestie lorem, et gravida enim.</p>
  </div>
  <div class="arrow-btn" style="right:4px;bottom:4px"><svg width="16" height="8" viewBox="0 0 18 8"><path d="M0 4h16M13 1l3 3-3 3" stroke="#fff" fill="none"/></svg></div>
</article>

<article class="post-sm" style="top:1888px">
  <div class="photo" role="img" aria-label="Photo of a red for sale sign in front of a house" style="background:linear-gradient(135deg,#5e7a4a 0%,#c8353a 45%,#b32a30 70%,#7b8a6a 100%)"></div>
  <div class="body">
    <span class="post-date">December 13, 2022</span>
    <h3>3 Ways Architects Can Build Better Cities</h3>
    <p>Lorem ipsum dolor sit amet, consectetur adipiscing elit. Ut non est mi.</p>
  </div>
  <div class="arrow-btn" style="right:4px;bottom:4px"><svg width="16" height="8" viewBox="0 0 18 8"><path d="M0 4h16M13 1l3 3-3 3" stroke="#fff" fill="none"/></svg></div>
</article>

<article class="post-sm" style="top:2097px">
  <div class="photo" role="img" aria-label="Photo of a couple reviewing house plans with an agent" style="background:linear-gradient(135deg,#3a4f6a 0%,#d7833e 40%,#e8d3b8 70%,#6a7c8c 100%)"></div>
  <div class="body">
    <span class="post-date">December 13, 2022</span>
    <h3>3 Ways Architects Can Build Better Cities</h3>
    <p>Lorem ipsum dolor sit amet, consectetur adipiscing elit. Ut non est mi.</p>
  </div>
  <div class="arrow-btn" style="right:4px;bottom:4px"><svg width="16" height="8" viewBox="0 0 18 8"><path d="M0 4h16M13 1l3 3-3 3" stroke="#fff" fill="none"/></svg></div>
</article>

<div class="about-photo" role="img" aria-label="Photo of an agent showing a couple a house with a red for sale sign"></div>
<section class="about-box">
  <h2>About Bright Haven Estate Sales</h2>
  <p>Welcome to Bright Haven Estate Sales. We have over 20 years of industry related experience. Lorem ipsum dolor sit amet, consectetur adipiscing elit. Ut non est mi. Vivamus luctus mi in odio volutpat, interdum bibendum magna commodo. Proin nec molestie lorem, et gravida enim. Proin iaculis et lorem a molestie. Mauris sit amet rutrum massa, non tempus tortor.</p>
  <p>Donec semper erat vitae consectetur dignissim. Cras lacinia hendrerit metus ac tristique. Donec auctor magna sed leo porta tincidunt. Mauris turpis lacus, rutrum et fringilla sit amet, malesuada non velit. Aenean accumsan tincidunt venenatis.</p>
  <div class="btn-gold">Read More</div>
</section>

<div class="faq-photo-frame"><div class="faq-photo" role="img" aria-label="Photo of a wooden toy house beside wooden blocks spelling FAQ"></div></div>
<section class="faq">
  <h2>Frequently asked questions</h2>
  <div class="faq-open">
    <div class="faq-q">What are the rules for real estate? <span>▲</span></div>
    <p>Indian real estate law does not envisage a system of land registration. Rather, the concept of registration is related to the documents under which the title is transferred from buyer to seller.</p>
  </div>
  <div class="faq-item" style="margin-top:6px"><span>How to do real estate sales?</span>▼</div>
  <div class="faq-item"><span>What is the process of property sale?</span>▼</div>
  <div class="faq-item"><span>What are the 5 golden rules of real estate?</span>▼</div>
  <div class="faq-item"><span>What is the minimum amount required for real estate?</span>▼</div>
  <div class="faq-item"><span>What is the law of real estate in India?</span>▼</div>
</section>

<div class="outline-word wordmark-band">BRIGHT HAVEN ESTATE SALES</div>

<section class="newsletter" role="img" aria-label="Purple toned photo of house keys on a table behind the newsletter signup">
  <h2>Want to get news and events from us?<br>Subscribe to our Newsletter here</h2>
  <div class="subscribe"><span>Enter your Email</span><div class="btn-gold">Subscribe</div></div>
</section>

<footer class="site-footer">
  <div class="brand"><span class="brand-mark"></span><span>Bright Haven Estate Sales</span></div>
  <p class="foot-about">Lorem ipsum dolor sit amet, consectetur adipiscing elit.</p>
  <div class="foot-col" style="left:308px;width:236px">
    <h4>Contact Us</h4>
    <ul>
      <li><span class="ico"></span>418 Maple Row, Nashville TN</li>
      <li style="margin-top:6px"><span class="ico"></span>615-555-0142</li>
      <li style="margin-top:6px"><span class="ico"></span>info@brighthavenestatesales.example</li>
    </ul>
  </div>
  <div class="foot-col" style="left:544px;width:195px;padding-left:60px">
    <h4>About Us</h4>
    <ul><li>Home</li><li>Services</li><li>Upcoming Sales</li><li>About Us</li><li>FAQs</li><li>Resources</li><li>Contact Us</li></ul>
  </div>
  <div class="foot-col" style="left:739px;width:190px;padding-left:60px">
    <h4>Services</h4>
    <ul><li>Estate Sales</li><li>Cleanouts</li><li>Appraisals</li></ul>
  </div>
  <div class="foot-col" style="left:929px;width:150px;padding-left:47px">
    <h4>Follow Us</h4>
    <ul>
      <li><span class="ico"></span>Friendbook</li>
      <li style="margin-top:7px"><span class="ico"></span>ViewTube</li>
      <li style="margin-top:7px"><span class="ico"></span>Chirper</li>
      <li style="margin-top:7px"><span class="ico"></span>Snapgram</li>
    </ul>
  </div>
  <div class="foot-rule"></div>
  <p class="copyright">© 2024 by Bright Haven Estate Sales All Rights Reserved</p>
</footer>

</body>
</html>
```